Hand Sanitizer Bottle Labels for new product launch

We are a small, U.S. based, family-owned paint company that has converted some of our capacity to make sanitizer to help out during the shortages related to the COVID-19 pandemic. Our product is bio-based (made from U.S.-grown corn), super clear and clean! It will be marketed to schools, businesses and other customers in the U.S.

We need help THIS WEEKEND to design product labels in a few basic sizes for pails/drums (label size 8.5x14"), round gallon jugs (like windshield washer fluid, label size 6.25x10"), round quarts (label size 5x11"), and 8oz (label size 5x7") and 6 ounce cylindrical bottles (label size 3x7", for samples). A portion (a third?) of the label on the right will need to be used for ingredient and warning text. We are looking for a design for the one gallon jug size for evaluation. Once a design concept (and designer) is chosen, that design will be scaled/reconfigured into the different sizes shown above.

We would like the design to communicate: simple, clean, fresh, natural -- and would prefer to use green and/or yellow primary colors in the design due to the bio-based focus.

Major features to highlight on packaging:
- 80% ethyl alcohol
- Bio-based
- Made in the USA (could use a graphic for this)
- QRV approved formula (could use a graphic for this)
- Kills most germs and bacteria

In small text, we would like to include the text: "QRV Registration 7162093418" somewhere on the label.

For examples of competitive labels, image search: "QRV hand sanitizer brands".

Files attached: brand logo, pic of some of the bottles to be labeled, Word doc showing our initial sample label which includes the QRV-required text.

Target Market(s)

American consumers of all ages

Font styles to use
Serif
Sans Serif

Colors
0a90cc
85cae6
00a990
86cfc6
cfeae6
d9e8a8
acd036
fbed22
fbee3f

Requirements
Must have
• Clean, fresh look - suitable for us on clear or white stock labels. Graphics to quickly communicate key features: QRV approved formula, Made in the USA, Bio-Based. Must include all required warning and descriptive text as shown on the sample label. Proportions of label must be able to conform to the label sizes mentioned in the summary above.
Nice to have
• Prefer use of greens, blues or yellows to communicate the product's clean and natural ingredients.

```html
<!DOCTYPE html>
<html lang="en">
<head>
<meta charset="utf-8">
<title>Hand Sanitiser Gallon Labels</title>
<link rel="stylesheet" href="https://fonts.googleapis.com/css2?family=Federo&family=Oswald:wght@600&family=Montserrat:wght@400;600;700&display=swap">
<style>
  :root {
    --backdrop: #d4d4d4;
    --jug-fill: #ffffff;
    --jug-line: #000000;
    --brand-blue: #0780bf;
    --brand-navy: #0b4466;
    --bio-green: #7cbf68;
    --bio-leaf: #3d8a3a;
    --claim-blue: #2f8fc4;
    --ink: #111111;
  }
  html, body {
    margin: 0;
    padding: 0;
    width: 1200px;
    height: 1200px;
    overflow: hidden;
    background: var(--backdrop);
  }
  .canvas { display: block; width: 1200px; height: 1200px; }
  .jug-body, .jug-cap { fill: var(--jug-fill); stroke: var(--jug-line); stroke-width: 7; stroke-linejoin: round; }
  .jug-outline { fill: none; stroke: var(--jug-line); stroke-width: 7; stroke-linejoin: round; }
  .jug-handle { fill: var(--backdrop); stroke: var(--jug-line); stroke-width: 6; }
  .water-band { fill: url(#water-tone); }
  .brand-name { font-family: "Montserrat", sans-serif; font-weight: 700; font-size: 26px; fill: var(--ink); text-anchor: middle; }
  .title-deco { font-family: "Federo", serif; text-anchor: middle; }
  .title-bold { font-family: "Oswald", sans-serif; font-weight: 600; text-anchor: middle; }
  .title-hand { fill: var(--brand-blue); }
  .title-sanitiser { fill: var(--brand-navy); }
  .bio-badge { fill: var(--bio-green); }
  .bio-drop { fill: var(--bio-leaf); }
  .bio-word { font-family: "Montserrat", sans-serif; font-weight: 600; fill: #ffffff; text-anchor: middle; }
  .claim { font-family: "Montserrat", sans-serif; font-size: 13px; fill: var(--ink); text-anchor: middle; }
  .claim-strong { font-weight: 700; }
  .claim-blue { font-family: "Montserrat", sans-serif; font-weight: 700; font-size: 13px; fill: var(--claim-blue); text-anchor: middle; }
  .volume { font-family: "Montserrat", sans-serif; font-weight: 600; fill: var(--ink); text-anchor: middle; }
</style>
</head>
<body>
<svg class="canvas" viewBox="0 0 2000 2000" xmlns="http://www.w3.org/2000/svg">
  <defs>
    <path id="jug-shape" d="M520 503 L738 503 C820 510 880 580 880 650 L880 1455 C880 1478 860 1497 835 1497 L415 1497 C390 1497 372 1478 372 1455 L372 675 C372 655 378 640 388 628 L468 530 C483 512 500 503 520 503 Z"/>
    <path id="jug-grip" d="M540 566 C548 566 550 580 550 590 L550 795 C550 805 546 812 540 818 L474 900 C466 908 456 911 448 909 C436 905 430 895 430 884 L430 672 C430 666 434 662 438 657 L484 601 C505 582 525 568 540 566 Z"/>
    <clipPath id="jug-clip">
      <path d="M520 503 L738 503 C820 510 880 580 880 650 L880 1455 C880 1478 860 1497 835 1497 L415 1497 C390 1497 372 1478 372 1455 L372 675 C372 655 378 640 388 628 L468 530 C483 512 500 503 520 503 Z"/>
    </clipPath>
    <linearGradient id="water-tone" x1="0" y1="0" x2="1" y2="1">
      <stop offset="0" stop-color="#0a5f7d"/>
      <stop offset="0.5" stop-color="#26bfe3"/>
      <stop offset="1" stop-color="#c4f4fb"/>
    </linearGradient>
  </defs>

  <g class="jug jug-deco">
    <rect class="jug-cap" x="555" y="425" width="202" height="78"/>
    <use class="jug-body" href="#jug-shape"/>
    <use class="jug-handle" href="#jug-grip"/>
    <text class="brand-name" x="632" y="978">Holland Grade</text>
    <text class="title-deco title-hand" x="632" y="1148" font-size="150" textLength="310" lengthAdjust="spacingAndGlyphs">HAND</text>
    <text class="title-deco title-sanitiser" x="632" y="1222" font-size="96" textLength="312" lengthAdjust="spacingAndGlyphs">SANITISER</text>
    <circle class="bio-badge" cx="632" cy="1293" r="52"/>
    <path class="bio-drop" d="M632 1250 C626 1260 622 1265 622 1270 A10 10 0 0 0 642 1270 C642 1265 638 1260 632 1250 Z"/>
    <text class="bio-word" x="632" y="1305" font-size="38">BIO</text>
    <text class="bio-word" x="634" y="1316" font-size="12" letter-spacing="5">BASED</text>
    <text class="claim" x="632" y="1393">80% <tspan class="claim-strong">ETHYL ALCOHOL</tspan></text>
    <text class="claim" x="632" y="1409">KILLS MOST <tspan class="claim-strong">GERMS AND BACTERIA</tspan></text>
    <text class="volume" x="632" y="1470" font-size="18">1 Gallon</text>
  </g>

  <g class="jug jug-bold" transform="translate(680 0)">
    <rect class="jug-cap" x="555" y="425" width="202" height="78"/>
    <use class="jug-body" href="#jug-shape"/>
    <g clip-path="url(#jug-clip)">
      <path class="water-band" role="img" aria-label="Splash of clear blue water with bubbles"
        d="M372 1438 C440 1440 500 1436 545 1410 C575 1392 600 1378 625 1380 C660 1384 690 1410 730 1420 C780 1430 830 1418 880 1420 L880 1500 L372 1500 Z"/>
    </g>
    <use class="jug-outline" href="#jug-shape"/>
    <use class="jug-handle" href="#jug-grip"/>
    <text class="brand-name" x="632" y="980">Holland Grade</text>
    <text class="title-bold title-hand" x="632" y="1170" font-size="165" textLength="292" lengthAdjust="spacingAndGlyphs">HAND</text>
    <text class="title-bold title-sanitiser" x="632" y="1243" font-size="92" textLength="292" lengthAdjust="spacingAndGlyphs">SANITISER</text>
    <text class="claim-blue" x="630" y="1297">BIO BASED</text>
    <text class="claim-blue" x="630" y="1312">80% ETHYL ALCOHOL</text>
    <text class="claim-blue" x="630" y="1327">KILLS MOST GERMS AND BACTERIA</text>
    <text class="volume" x="636" y="1466" font-size="14">1 Gallon / 128 Oz</text>
  </g>
</svg>
</body>
</html>
```